QKB Coffee Company - design for coffee company logo and 12 oz coffee bags

I would like to start selling coffee and need both a brand logo as well as packaging design for the coffee bags. The name of the company is QKB Coffee Company. I have a related brand for a youtube channel called QKBM0TE, I will attach that logo to the uploaded files. The branding for the coffee should compliment QKBM0TE, but doesn't have to (and probably should NOT be too close in similarity). The Company Brand logo should be featured on the bag, but not as dominant/large as the specific product label (like Harbor 3056).
This coffee will be marketed towards aviation consumers. Pilots, dispatchers, ATC professionals, mechanics, etc. Male dominated market. Masculine themes needed.
For the bag design, I need one standard bag design to use across all my products, then I will simply add the SKU product names to all the interchangeable bags. So my design request is for a dark bag with airspace lines/designs/graphics in a repeatable format that I can cast to the printing design. I am adding inspiration upload for this. I'm thinking using a light or white color for the shapes/vectors/symbols on the dark bag. Not all of the different shapes and icons should be included, but things like the compass circle with tick marks, line vectors stretching out in different directions. Again - don't need ALL of the shapes and text. certainly not the green stuff. And important to note, the inspiration uploads I've provided have white background and darker lines/shapes. I would like to inverse that for this design. Dark bag and light shapes/lines.
If you could include the first product label for the bag, that would be great. The first coffee product will be called "Harbor 3056". I've included an example I tried to make on Figma, but I'm an awful designer. The example I included has the "1200" on an aviation transponder. This is the code plugged into the airplane that lets ATC know who you are and where you are. In the final delivery, I would like the product label (Harbor 3056) to be separate from the bag itself so I can change it out with other coffee product labels for my light and dark roasts. A section at the bottom with roast profile, grind type, source, etc should be located on the bottom (or wherever it makes sense). The inspiration for the layout could come from the lower section of the Approach Plate i attached.
On the back, a section that notes details about the company:
"QKB Coffee Company was built for people who start the day with somewhere to go — pilots, builders, travelers, early risers, and anyone chasing the next leg of the journey.
QKB is a nod to our home skies under Pell Ridge Center and to Quantity Kept Below — the aviation reminder that every mission starts with what you choose to carry.
Fuel Your Mission."

Where the package opens at the top, a horizontal image that says "REMOVE BEFORE FLIGHT" is a nice to have. Inspiration image uploaded to the brief. This is a standard cover on aircraft to protect sensitive instruments/equipment. Located right where the folded seal of the bag is would be a nice touch. Red with white text.

Target Market(s)

aviation professionals and enthusiasts... who like coffee. Pilots, dispatchers, military, Air Traffic Control, Mechanics. Mostly male crowd.

Industry/Entity Type

Coffee company, but aviation style branding

Requirements
Nice to have
• company tagline "Fuel Your Mission" - experiment with placing - either under company logo - on sides/back - whatever looks/feels right.
Should not have
• do not include the uploaded QKB M0TE logo on the package. It's for reference as a sister brand only.

```html
<!DOCTYPE html>
<html lang="en">
<head>
<meta charset="utf-8">
<title>QKB Coffee Company — Harbor 3056 Packaging</title>
<link rel="stylesheet" href="https://fonts.googleapis.com/css2?family=Oswald:wght@500;700&family=Barlow+Condensed:wght@400;500;600&family=Share+Tech+Mono&display=swap">
<style>
  :root {
    --stage: #0c0c0d;
    --bag: #1c1c1e;
    --bag-deep: #141415;
    --ink: #151515;
    --paper: #dedcd8;
    --paper-line: #a9a7a3;
    --red: #c8191f;
    --red-led: #e0262b;
    --white: #f1f0ed;
    --muted: #b9b8b4;
    --line: #4a4a4c;
  }
  * { box-sizing: border-box; margin: 0; padding: 0; }
  html, body { width: 1200px; height: 800px; overflow: hidden; background: var(--stage); }
  body { position: relative; font-family: "Barlow Condensed", sans-serif; color: var(--white); }

  .bag { position: absolute; top: 30px; width: 400px; height: 720px; border-radius: 6px; overflow: hidden; }
  .bag--front { left: 30px; }
  .bag--back { left: 455px; width: 395px; }
  .bag__chart { position: absolute; inset: 0; background: radial-gradient(circle at 40% 30%, #2a2a2c, var(--bag) 55%, var(--bag-deep)); }

  .flight-tag { position: absolute; top: 16px; left: 20px; display: flex; align-items: center; }
  .flight-tag__ring { width: 34px; height: 34px; border: 4px solid #8d8d90; border-radius: 50%; margin-right: -6px; z-index: 1; }
  .flight-tag__band { background: var(--red); width: 300px; height: 44px; display: flex; align-items: center; justify-content: center;
    font-family: "Oswald", sans-serif; font-weight: 700; font-size: 27px; letter-spacing: 0.5px; color: var(--white); border-radius: 3px; }

  .brand { position: absolute; top: 215px; left: 0; right: 0; text-align: center; }
  .brand__name { font-family: "Oswald", sans-serif; font-weight: 700; font-size: 62px; letter-spacing: 6px; color: var(--white); line-height: 1; }
  .brand__sub { margin-top: 12px; font-family: "Oswald", sans-serif; font-weight: 500; font-size: 20px; letter-spacing: 5px; }
  .brand__tagline { margin-top: 8px; font-size: 16px; letter-spacing: 3px; color: var(--red); font-weight: 600; }
  .brand__tagline::before, .brand__tagline::after { content: ""; display: inline-block; width: 26px; height: 1.5px; background: var(--red); vertical-align: middle; margin: 0 10px; }

  /* product label */
  .label { position: absolute; left: 22px; right: 22px; top: 420px; background: var(--paper); color: var(--ink); border-radius: 8px; overflow: hidden; }
  .label__head { display: flex; align-items: center; justify-content: space-between; gap: 10px; padding: 12px 12px 10px 14px; border-bottom: 1px solid var(--paper-line); }
  .product-name { font-family: "Oswald", sans-serif; font-weight: 700; line-height: 0.95; }
  .product-name__word { font-size: 34px; color: var(--ink); display: block; }
  .product-name__code { font-size: 54px; color: var(--red); display: block; }

  .transponder { background: #222224; border-radius: 8px; padding: 8px; box-shadow: inset 0 0 0 2px #3a3a3c; }
  .transponder__screen { background: #0a0a0a; border-radius: 4px; display: flex; align-items: center; justify-content: space-between; padding: 6px 10px; }
  .transponder__mode { font-family: "Barlow Condensed", sans-serif; font-size: 12px; color: var(--red-led); }
  .transponder__code { font-family: "Share Tech Mono", monospace; font-size: 34px; color: var(--red-led); letter-spacing: 3px; }
  .transponder__keys { display: flex; gap: 4px; margin-top: 7px; }
  .transponder__key { background: #0e0e0f; color: var(--muted); font-size: 10px; border-radius: 3px; width: 14px; height: 17px; display: flex; align-items: center; justify-content: center; border: 1px solid #444; }
  .transponder__key--ident { width: 26px; font-size: 7px; }

  .spec-row { display: flex; border-bottom: 1px solid var(--paper-line); }
  .spec { padding: 7px 10px; border-right: 1px solid var(--paper-line); flex: 1; position: relative; }
  .spec:last-child { border-right: none; }
  .spec__key { font-size: 13px; font-weight: 500; color: #333; letter-spacing: 0.5px; }
  .spec__val { font-size: 14px; font-weight: 600; color: #222; text-transform: uppercase; line-height: 1.2; }
  .spec__val--red { color: var(--red); }
  .spec__icon { position: absolute; right: 8px; top: 50%; transform: translateY(-50%); }
  .roast-meter { display: flex; gap: 3px; margin-top: 3px; }
  .roast-meter span { width: 10px; height: 8px; border: 1px solid var(--red); }
  .roast-meter .on { background: var(--red); }

  .label__foot { background: var(--ink); color: var(--white); text-align: center; font-size: 14px; letter-spacing: 2px; padding: 9px; }

  /* back panel */
  .story { position: absolute; top: 150px; left: 40px; right: 40px; border: 1px solid var(--line); border-radius: 14px; background: rgba(20,20,21,0.92); padding: 18px 22px 16px; }
  .story__title { font-family: "Oswald", sans-serif; font-weight: 500; font-size: 16px; letter-spacing: 1.5px; }
  .story__title::before { content: "★"; color: var(--red); margin-right: 6px; }
  .story__text { font-size: 14px; line-height: 1.5; color: var(--white); margin-top: 4px; }
  .story__rule { border: none; border-top: 1px solid var(--line); margin: 12px 0; }
  .story__tagline { color: var(--red); font-family: "Oswald", sans-serif; font-size: 16px; letter-spacing: 1.5px; margin-top: 12px; }
  .values { display: flex; border-top: 1px solid var(--line); border-bottom: 1px solid var(--line); margin-top: 12px; padding: 12px 0; }
  .value { flex: 1; text-align: center; font-size: 10.5px; letter-spacing: 0.5px; color: var(--muted); border-right: 1px solid var(--line); }
  .value:last-child { border-right: none; }
  .value svg { display: block; margin: 0 auto 8px; }
  .contact { display: flex; align-items: center; justify-content: space-between; margin-top: 14px; font-size: 13px; letter-spacing: 1.5px; }
  .contact__dots { display: flex; gap: 10px; }
  .contact__dots span { width: 18px; height: 18px; border: 1.5px solid var(--white); border-radius: 50%; }

  /* standalone label card */
  .label-card { position: absolute; left: 880px; top: 140px; width: 290px; height: 600px; background: #1a1a1b; border-radius: 16px; padding: 12px; border: 1px solid #333; }
  .label-card__inner { background: var(--paper); color: var(--ink); border-radius: 8px; height: 100%; display: flex; flex-direction: column; overflow: hidden; }
  .label-card__title { text-align: center; padding-top: 12px; }
  .label-card__title .product-name__word { font-size: 44px; }
  .label-card__title .product-name__code { font-size: 72px; }
  .label-card .transponder { margin: 10px 12px 12px; }
  .label-card .transponder__code { font-size: 44px; }
  .label-card .transponder__key { width: 19px; height: 20px; }
  .label-card .transponder__key--ident { width: 32px; }
  .label-card .spec-row { border-top: 1px solid var(--paper-line); border-bottom: none; }
  .label-card .spec { padding: 8px 12px; }
  .label-card .spec__val { font-size: 16px; }
  .label-card .spec__key { font-size: 14px; }
  .stamp { position: absolute; right: 14px; top: 50%; transform: translateY(-50%); width: 50px; height: 50px; border: 2px solid var(--ink); border-radius: 50%; }
  .label-card__foot { margin-top: auto; background: var(--ink); color: var(--red); text-align: center; font-size: 15px; letter-spacing: 2px; padding: 12px 0 14px; }
</style>
</head>
<body>

<!-- Front of bag -->
<section class="bag bag--front">
  <div class="bag__chart" role="img" aria-label="Light aeronautical chart pattern of airway lines, fixes and a compass rose on the dark bag"></div>
  <div class="flight-tag"><span class="flight-tag__ring"></span><span class="flight-tag__band">REMOVE BEFORE FLIGHT</span></div>

  <div class="brand">
    <div class="brand__name">QKB</div>
    <div class="brand__sub">COFFEE COMPANY</div>
    <div class="brand__tagline">FUEL YOUR MISSION</div>
  </div>

  <div class="label">
    <div class="label__head">
      <h1 class="product-name"><span class="product-name__word">HARBOR</span><span class="product-name__code">3056</span></h1>
      <div class="transponder">
        <div class="transponder__screen"><span class="transponder__mode">ALT</span><span class="transponder__code">3056</span></div>
        <div class="transponder__keys">
          <span class="transponder__key">0</span><span class="transponder__key">1</span><span class="transponder__key">2</span><span class="transponder__key">3</span><span class="transponder__key">4</span><span class="transponder__key">5</span><span class="transponder__key">6</span><span class="transponder__key">7</span><span class="transponder__key transponder__key--ident">IDENT</span>
        </div>
      </div>
    </div>
    <div class="spec-row">
      <div class="spec"><div class="spec__key">ROAST</div><div class="spec__val spec__val--red">Dark</div>
        <div class="roast-meter"><span class="on"></span><span class="on"></span><span class="on"></span><span></span><span></span></div></div>
      <div class="spec"><div class="spec__key">GRIND</div><div class="spec__val spec__val--red">Whole Bean</div>
        <svg class="spec__icon" width="18" height="22" viewBox="0 0 18 22"><ellipse cx="9" cy="11" rx="7" ry="10" fill="#151515" transform="rotate(25 9 11)"/><path d="M5 18 Q10 11 13 4" stroke="#dedcd8" stroke-width="1.5" fill="none"/></svg></div>
      <div class="spec"><div class="spec__key">ORIGIN</div><div class="spec__val" style="font-size:12.5px">Central &amp;<br>South America</div>
        <svg class="spec__icon" width="24" height="24" viewBox="0 0 24 24" fill="none" stroke="#151515" stroke-width="1.6"><circle cx="12" cy="12" r="10"/><ellipse cx="12" cy="12" rx="4.5" ry="10"/><path d="M2 12h20M4 7h16M4 17h16"/></svg></div>
    </div>
    <div class="spec-row" style="border-bottom:none">
      <div class="spec" style="flex:1.7"><div class="spec__key">TASTE PROFILE</div><div class="spec__val" style="font-size:13px">Dark Chocolate <span style="color:var(--red)">•</span> Caramel <span style="color:var(--red)">•</span> Smoke</div></div>
      <div class="spec"><div class="spec__key">NET WT.</div><div class="spec__val" style="font-size:17px">12oz (340g)</div></div>
    </div>
    <div class="label__foot">★ ROASTED IN THE USA ★</div>
  </div>
</section>

<!-- Back of bag -->
<section class="bag bag--back">
  <div class="bag__chart" role="img" aria-label="Light aeronautical chart pattern of airway lines, fixes and a compass rose on the dark bag"></div>
  <div class="flight-tag"><span class="flight-tag__ring"></span><span class="flight-tag__band">REMOVE BEFORE FLIGHT</span></div>

  <article class="story">
    <h2 class="story__title">MISSION</h2>
    <p class="story__text">QKB Coffee Company was built for people who start the day with somewhere to go — pilots, builders, travelers, early risers, and anyone chasing the next leg of the journey.</p>
    <hr class="story__rule">
    <h2 class="story__title">ORIGIN</h2>
    <p class="story__text">QKB is a nod to our home skies under Pell Ridge Center and to Quantity Kept Below — the aviation reminder that every mission starts with what you choose to carry.</p>
    <p class="story__tagline">FUEL YOUR MISSION.</p>
    <div class="values">
      <div class="value">
        <svg width="34" height="30" viewBox="0 0 34 30" fill="none" stroke="#f1f0ed" stroke-width="1.6" stroke-linejoin="round"><path d="M4 26 L30 4 M14 10 L3 11 L9 15 M22 18 L21 28 L17 22 M26 6 L30 4 L28 8"/></svg>
        ROASTED FOR<br>PERFORMANCE</div>
      <div class="value">
        <svg width="40" height="30" viewBox="0 0 40 30" fill="none" stroke="#f1f0ed" stroke-width="1.6" stroke-linejoin="round"><path d="M2 26 L16 6 L22 14 L27 9 L38 26 Z M13 11 L16 14 L19 10"/></svg>
        HIGH ALTITUDE<br>APPROVED</div>
      <div class="value">
        <svg width="30" height="30" viewBox="0 0 30 30" fill="none" stroke="#f1f0ed" stroke-width="1.8"><path d="M5 18 V14 a10 10 0 0 1 20 0 V18"/><rect x="3" y="16" width="5" height="8" rx="1.5"/><rect x="22" y="16" width="5" height="8" rx="1.5"/><path d="M24 24 Q24 28 17 28"/></svg>
        QUALITY<br>FIRST</div>
    </div>
    <div class="contact"><span>QKBCOFFEE.COM</span><span class="contact__dots"><span></span><span></span></span></div>
  </article>
</section>

<!-- Interchangeable product label -->
<section class="label-card">
  <div class="label-card__inner">
    <h2 class="product-name label-card__title"><span class="product-name__word">HARBOR</span><span class="product-name__code">3056</span></h2>
    <div class="transponder">
      <div class="transponder__screen"><span class="transponder__mode">ALT</span><span class="transponder__code">3056</span></div>
      <div class="transponder__keys">
        <span class="transponder__key">0</span><span class="transponder__key">1</span><span class="transponder__key">2</span><span class="transponder__key">3</span><span class="transponder__key">4</span><span class="transponder__key">5</span><span class="transponder__key">6</span><span class="transponder__key">7</span><span class="transponder__key transponder__key--ident">IDENT</span>
      </div>
    </div>
    <div class="spec-row">
      <div class="spec"><div class="spec__key">ROAST</div><div class="spec__val spec__val--red">Dark</div>
        <div class="roast-meter"><span class="on"></span><span class="on"></span><span class="on"></span><span></span><span></span></div></div>
      <div class="spec"><div class="spec__key">GRIND</div><div class="spec__val spec__val--red">Whole Bean</div>
        <svg class="spec__icon" width="18" height="22" viewBox="0 0 18 22"><ellipse cx="9" cy="11" rx="7" ry="10" fill="#151515" transform="rotate(25 9 11)"/><path d="M5 18 Q10 11 13 4" stroke="#dedcd8" stroke-width="1.5" fill="none"/></svg></div>
    </div>
    <div class="spec-row">
      <div class="spec"><div class="spec__key">ORIGIN</div><div class="spec__val">Central &amp; South America</div>
        <svg class="spec__icon" width="28" height="28" viewBox="0 0 24 24" fill="none" stroke="#151515" stroke-width="1.6"><circle cx="12" cy="12" r="10"/><ellipse cx="12" cy="12" rx="4.5" ry="10"/><path d="M2 12h20M4 7h16M4 17h16"/></svg></div>
    </div>
    <div class="spec-row">
      <div class="spec"><div class="spec__key">TASTE PROFILE</div><div class="spec__val">Dark Chocolate<br>Caramel <span style="color:var(--red)">•</span> Smoke</div></div>
    </div>
    <div class="spec-row">
      <div class="spec"><div class="spec__key">NET WT.</div><div class="spec__val">12oz (340g)</div><span class="stamp"></span></div>
    </div>
    <div class="label-card__foot">FOR AVIATORS. BY AVIATORS.</div>
  </div>
</section>

</body>
</html>
```